Hearing Aid Postcard

Need a large easy to read postcard for seniors ages 65-85. Postcard is a City Hearing Event with lots of free offers. Seniors identify pictures so we need large photos and loud "ON SALE" and "FREE Hearing Exam" headlines. Please use the attached sample postcard as a reference only for copy and the types of photos styles we like. Please use your personal creativity in designing a postcard that includes the information provided. Thank You very much for your Help!

Target Market(s)

Seniors ages 65 to 85

Industry/Entity Type

Hearing Aid

Font styles to use
Sans Serif

Requirements
Must have
• See Proect discription...

```html
<!DOCTYPE html>
<html lang="en">
<head>
<meta charset="utf-8">
<title>Hearing Aid Postcard</title>
<link rel="stylesheet" href="https://fonts.googleapis.com/css2?family=Anton&family=Exo+2:wght@500&family=Montserrat:ital,wght@0,500;0,800;1,900&family=Roboto:wght@400;500;700&display=swap">
<style>
:root{
  --board:#9b9b9b;
  --ink:#000;
  --paper:#fff;
  --navy:#0a1f5c;
  --navy-deep:#06143d;
  --blue:#0d3f8f;
  --teal:#2ec7c0;
  --red:#c8102e;
  --maroon:#7e0a0f;
  --yellow:#ffff00;
  --gold:#ffd21f;
  --orange:#ff7a00;
  --white:#fff;
}
*{margin:0;padding:0;box-sizing:border-box}
html,body{width:1200px;height:642px;overflow:hidden;background:var(--board)}
.board{position:relative;width:1200px;height:642px;background:var(--board)}
.board-title{position:absolute;top:40px;left:0;width:1200px;text-align:center;font:400 74px/1 Arial,Helvetica,sans-serif;color:var(--ink)}
.card-frame{position:absolute;top:188px;width:505px;height:384px;background:var(--paper)}
.card-frame.front{left:70px}
.card-frame.back{left:613px}
.card{position:absolute;left:12px;top:12px;width:481px;height:360px;overflow:hidden}
.abs{position:absolute}
.anton{font-family:Anton,"Arial Narrow",sans-serif;font-weight:400}

/* front */
.front .card{background:linear-gradient(120deg,var(--navy-deep) 0%,var(--blue) 40%,#0b2f73 60%,var(--navy-deep) 100%)}
.sale-tab{left:0;top:0;width:212px;height:50px;background:var(--red);border-radius:0 0 14px 0;box-shadow:3px 3px 0 #8a0a1e}
.sale-tab span{position:absolute;left:17px;top:2px;font:italic 900 39px/1.15 Montserrat,sans-serif;color:var(--white);letter-spacing:-1px}
.free-word{left:12px;top:54px;font:italic 900 58px/1 Montserrat,sans-serif;background:linear-gradient(180deg,#8ff5ee,var(--teal) 55%,#138f99);-webkit-background-clip:text;background-clip:text;color:transparent;letter-spacing:-1px}
.dont-miss{left:226px;top:8px;font-size:30px;line-height:31px;color:var(--white)}
.dates{color:var(--yellow);line-height:1;white-space:nowrap}
.front .dates{left:298px;top:9px;font-size:29px}
.insurance-card{left:291px;top:46px;width:58px;height:58px;border-radius:50%;border:3px solid #e8e8e8;background:linear-gradient(160deg,#fff,#c9ccd3 70%,#2a2d36)}
.insurance-note{left:356px;top:55px;font-size:16px;line-height:20px;color:var(--white)}
.services{left:12px;top:112px;width:180px}
.service{position:relative;height:36px;padding-left:26px}
.service-icon{position:absolute;left:0;top:2px;width:23px;height:23px;background:var(--white);border-radius:3px;border:1px solid #9bb;display:flex;align-items:center;justify-content:center}
.service h3{font:500 12.5px/1 "Exo 2",sans-serif;color:var(--yellow);white-space:nowrap}
.service p{font:500 7px/8.5px Roboto,sans-serif;color:var(--white);margin-top:2px}
.free-exam{left:15px;top:258px;font-size:24px;color:var(--white);line-height:1.1}
.photo-curve{left:195px;top:112px;width:290px;height:176px}
.price-badge{left:195px;top:110px;width:104px;height:56px}
.new-tag{left:205px;top:110px;width:28px;height:11px;background:var(--red);transform:skewX(-12deg);font:italic 900 7px/11px Montserrat,sans-serif;color:var(--white);text-align:center}
.price{left:211px;top:123px;font-size:30px;color:var(--red);line-height:1;white-space:nowrap}
.price small{font:500 5px Roboto,sans-serif;color:#000}
.price sup{font:700 10px Roboto,sans-serif;color:#000;vertical-align:14px}
.price .ea{font:400 5px Roboto,sans-serif;color:#000}
.price-terms{left:204px;top:150px;width:82px;font:700 3.6px/4.5px Roboto,sans-serif;color:var(--white);text-transform:uppercase}
.footer{left:0;bottom:0;height:66px;background:var(--maroon)}
.front .footer{width:481px}
.footer-label{font:500 10px/1 Montserrat,sans-serif;color:var(--white);white-space:nowrap}
.presenter-photo{left:12px;top:316px;width:54px;height:39px;background:linear-gradient(120deg,#6b8fb8,#d8c6b8 60%,#9aa8b8)}
.presenter-text{left:70px;top:316px;width:119px;font:400 4.2px/5.8px Roboto,sans-serif;color:#f1dcdc;text-align:justify}
.rating{left:200px;width:60px;height:16px}
.rating .dot{position:absolute;left:0;top:1px;width:13px;height:13px;border-radius:50%;background:var(--white)}
.rating .name{position:absolute;left:17px;top:0;font:700 5px/1 Roboto,sans-serif;color:var(--white)}
.rating .stars{position:absolute;left:17px;top:5px;font:700 6px/1 Roboto,sans-serif;color:var(--gold);letter-spacing:.5px}
.rating .score{position:absolute;left:17px;top:11px;font:700 5px/1 Montserrat,sans-serif;color:var(--white)}
.review{left:258px;width:76px;font:400 3.6px/4.4px Roboto,sans-serif;color:#f1dcdc}
.review b{display:block;font:500 4.3px/5px Roboto,sans-serif;color:var(--white)}
.review::before{content:"";position:absolute;left:-5px;top:0;width:4px;height:4px;border-radius:50%;background:var(--white)}
.appt{width:100px;height:22px;background:var(--yellow);font:400 10.5px/22px Anton,sans-serif;font-style:italic;color:#111;text-align:center;white-space:nowrap;overflow:hidden}
.appt-arrow{width:20px;height:22px;background:var(--orange)}
.phone{display:flex;align-items:center;gap:3px;font-size:16.5px;color:var(--white);line-height:1;white-space:nowrap}

/* back */
.back .card{background:linear-gradient(180deg,var(--navy-deep) 0%,#10316f 45%,#1b6b8f 100%)}
.event-title{left:18px;top:24px;font-size:64px;line-height:1;color:var(--white);white-space:nowrap;transform:scaleX(1.27);transform-origin:left top}
.city{left:60px;top:18px;font-size:17px;line-height:1;color:var(--gold);letter-spacing:2.5px;z-index:2}
.back .dates{left:261px;top:96px;font-size:33px}
.event-photo{left:0;top:98px;width:320px;height:196px;background:radial-gradient(ellipse at 55% 45%,#d9b49a 0%,#8a7e82 35%,#23406f 75%,rgba(20,50,100,0) 100%)}
.map-box{left:304px;top:136px;width:162px;height:150px;background:var(--red);border:2px solid var(--white);border-radius:10px;overflow:hidden}
.map-head{text-align:center;padding-top:4px;color:var(--white);font:800 15px/1 Montserrat,sans-serif}
.map-head span{display:block;font-size:11px;color:var(--gold);margin-top:1px}
.map-area{position:absolute;left:0;top:31px;width:158px;height:117px;background:linear-gradient(135deg,#efe7d6,#e2d8bf);border-radius:0 0 8px 8px}
.back .footer{width:240px}
.sale-stack{left:8px;top:302px;font:italic 900 25px/25px Montserrat,sans-serif;color:var(--white)}
.back .blank{left:240px;top:294px;width:241px;height:66px;background:var(--paper)}
</style>
</head>
<body>
<div class="board">
  <h1 class="board-title">Hearing Aid Postcard</h1>

  <div class="card-frame front">
    <div class="card">
      <div class="abs sale-tab"><span>ON SALE</span></div>
      <div class="abs free-word">FREE</div>
      <div class="abs anton dont-miss">Don't<br>Miss<br>Out!</div>
      <div class="abs anton dates">April 13th - 23rd</div>
      <div class="abs insurance-card" role="img" aria-label="Healthcare discount card"></div>
      <div class="abs anton insurance-note">Works Better Than<br>Some Insurances!</div>

      <div class="abs services">
        <div class="service">
          <div class="service-icon" role="img" aria-label="Ear inspection icon"></div>
          <h3>Otoscopic Ear Inspection</h3>
          <p>We'll examine your ears to see exactly<br>what may be causing your hearing loss</p>
        </div>
        <div class="service">
          <div class="service-icon" role="img" aria-label="Hearing evaluation icon"></div>
          <h3>Hearing Evaluation</h3>
          <p>This audiometric assessment will<br>accurately reveal your hearing loss</p>
        </div>
        <div class="service">
          <div class="service-icon" role="img" aria-label="Hearing aid device icon"></div>
          <h3>Product Demonstrations</h3>
          <p>Experience the power of the newest<br>groundbreaking technology firsthand</p>
        </div>
        <div class="service">
          <div class="service-icon"><svg width="15" height="15" viewBox="0 0 15 15"><path d="M2 8 L6 12 L13 2" fill="none" stroke="#0a1f5c" stroke-width="2.6" stroke-linecap="round"/></svg></div>
          <h3>Clean &amp; Check</h3>
          <p>We'll examine and thoroughly clean your<br>hearing aids during your visit</p>
        </div>
      </div>

      <div class="abs anton free-exam">FREE Hearing Exam</div>

      <svg class="abs photo-curve" viewBox="0 0 290 176" role="img" aria-label="Photo of a hearing specialist fitting a hearing aid for a patient">
        <defs>
          <linearGradient id="exam-photo" x1="0" y1="0" x2="1" y2="1">
            <stop offset="0" stop-color="#eef1f4"/>
            <stop offset=".5" stop-color="#b9c3cc"/>
            <stop offset="1" stop-color="#e7d2c3"/>
          </linearGradient>
        </defs>
        <path d="M30 2 H290 V176 H80 C20 150 0 110 0 70 C0 40 10 15 30 2 Z" fill="#fff"/>
        <path d="M34 6 H290 V176 H84 C26 150 5 110 5 72 C5 44 15 20 34 6 Z" fill="url(#exam-photo)"/>
      </svg>

      <svg class="abs price-badge" viewBox="0 0 104 56" aria-hidden="true">
        <path d="M8 4 H104 L88 46 H0 Z" fill="#fff"/>
        <path d="M3 40 H90 L86 54 H0 Z" fill="#0d3f8f"/>
      </svg>
      <div class="abs new-tag">NEW!</div>
      <div class="abs anton price"><small>Just </small><sup>$</sup>495<span class="ea">ea.</span></div>
      <div class="abs price-terms">Limit two, not valid with any other offer. Offer expires April 28th, 2025</div>

      <div class="abs footer">
        <div class="abs footer-label" style="left:11px;top:6px">Event Presented By</div>
        <div class="abs footer-label" style="left:200px;top:6px">Friendbook &amp; Searchly review</div>
      </div>
      <div class="abs presenter-photo" role="img" aria-label="Photo of the hearing care team with a patient"></div>
      <p class="abs presenter-text">Lorem ipsum dolor sit amet, consectetur adipiscing elit. Nulla malesuada nibh eu scelerisque porttitor. Fusce elementum accumsan suscipit. Sed dapibus accumsan leo ut porta. Donec in sapien dignissim, tempus elit sit amet, egestas nunc. Cras quis est at lacus euismod mollis eu sed turpis. Integer eleifend eros eu metus efficitur, in imperdiet nulla rutrum.</p>

      <div class="abs rating" style="top:324px"><span class="dot"></span><span class="name">Friendbook</span><span class="stars">★★★★★</span><span class="score">5.0 RATING</span></div>
      <div class="abs rating" style="top:344px"><span class="dot"></span><span class="name">Searchly</span><span class="stars">★★★★★</span><span class="score">5.0 RATING</span></div>
      <p class="abs review" style="top:318px"><b>Marcus Delaney</b>Lorem ipsum dolor sit amet, consectetur adipiscing elit. Nulla malesuada nibh eu scelerisque porttitor.</p>
      <p class="abs review" style="top:338px"><b>Nora Whitfield</b>Lorem ipsum dolor sit amet, consectetur adipiscing elit. Nulla malesuada nibh eu scelerisque porttitor.</p>

      <div class="abs appt" style="left:344px;top:306px">Appointments Limited!</div>
      <svg class="abs appt-arrow" style="left:447px;top:306px" viewBox="0 0 20 22" aria-hidden="true"><path d="M7 5 L13 11 L7 17" fill="none" stroke="#fff" stroke-width="2.6"/></svg>
      <div class="abs anton phone" style="left:344px;top:334px">
        <svg width="15" height="15" viewBox="0 0 24 24" aria-hidden="true"><path d="M6.6 10.8a15 15 0 0 0 6.6 6.6l2.2-2.2a1 1 0 0 1 1-.25 11.4 11.4 0 0 0 3.6.57 1 1 0 0 1 1 1V20a1 1 0 0 1-1 1A17 17 0 0 1 3 4a1 1 0 0 1 1-1h3.5a1 1 0 0 1 1 1c0 1.25.2 2.45.57 3.57a1 1 0 0 1-.25 1z" fill="#fff"/></svg>
        1 (555) 010-4827
      </div>
    </div>
  </div>

  <div class="card-frame back">
    <div class="card">
      <div class="abs event-photo" role="img" aria-label="Photo of an audiologist examining a senior man's ear with an otoscope"></div>
      <div class="abs anton event-title">Hearing Event</div>
      <div class="abs anton city">BROOKVILLE</div>
      <div class="abs anton dates">April 13th - 23rd</div>

      <div class="abs map-box">
        <div class="map-head">JUST 4.2 MILES<span>FROM 12345 MY STREET</span></div>
        <div class="map-area" role="img" aria-label="Street map showing the route to the event"></div>
      </div>

      <div class="abs footer"></div>
      <div class="abs blank"></div>
      <div class="abs sale-stack">ON<br>SALE</div>
      <div class="abs appt" style="left:92px;top:306px">Appointments Limited!</div>
      <svg class="abs appt-arrow" style="left:195px;top:306px" viewBox="0 0 20 22" aria-hidden="true"><path d="M7 5 L13 11 L7 17" fill="none" stroke="#fff" stroke-width="2.6"/></svg>
      <div class="abs anton phone" style="left:92px;top:334px">
        <svg width="15" height="15" viewBox="0 0 24 24" aria-hidden="true"><path d="M6.6 10.8a15 15 0 0 0 6.6 6.6l2.2-2.2a1 1 0 0 1 1-.25 11.4 11.4 0 0 0 3.6.57 1 1 0 0 1 1 1V20a1 1 0 0 1-1 1A17 17 0 0 1 3 4a1 1 0 0 1 1-1h3.5a1 1 0 0 1 1 1c0 1.25.2 2.45.57 3.57a1 1 0 0 1-.25 1z" fill="#fff"/></svg>
        1 (555) 010-4827
      </div>
    </div>
  </div>
</div>
</body>
</html>
```